Web Design Project

We are an aircraft maintenance company servicing small aircraft - both single and twin engines.
we are new business owners and prior to this, no marketing has been done in the business.
We provide superior workmanship, excellent customer service and are there every step of the way for owners of aircraft from purchase through to all the maintenance required on their aircraft.
We are based in Mackay, Queesland, Australia and can service aircraft from around the country.
We also provide a spray painting service and operate in a large hangar at the General aviation section of Brindle Field airport.
We love our industry and are third generation in the aviation business. Most of our clients are either operating aircraft in tourism or charter/flight schools or are aviation enthusiasts who love flying.
We have both used Joomla before and like this as we can easily update information in it.
We like sections to be Home, About Us, Services/Capability, Gallery and Contact us
Please feel free to get in touch if you require more information or if there is a question you'd like to ask about us.
Our logo is attached. This is about to be changed only slightly but inserting a new aircraft. Our colours are navy, red, white and grey.
We like the idea of a blue background/navy background as this looks good on website and is a good colour for an aviation company.
thanks,
Maren
Target Market(s)
owners/operators of small aircraft within Australia, mostly in Queensland.
Industry/Entity Type
Marketing
Look and feel

```html
<!DOCTYPE html>
<html lang="en">
<head>
<meta charset="utf-8">
<title>Corvale Air Aircraft Maintenance</title>
<link rel="stylesheet" href="https://fonts.googleapis.com/css2?family=Open+Sans:wght@400;600;700&display=swap">
<style>
  :root {
    --navy: #1b0c63;
    --navy-soft: #2a1c78;
    --grey: #c9c9cb;
    --grey-light: #f1f1f1;
    --red: #e31b2a;
    --white: #ffffff;
    --ink: #1a1a1a;
    --ink-soft: #444444;
    --caption-bg: rgba(28, 30, 38, 0.88);
  }
  * { margin: 0; padding: 0; box-sizing: border-box; }
  html, body { width: 1121px; height: 1200px; overflow: hidden; background: var(--white); }
  body { font-family: "Open Sans", Arial, sans-serif; color: var(--ink); }
  .page { position: relative; width: 1121px; height: 1200px; overflow: hidden; }

  .site-header { position: absolute; left: 0; top: 0; width: 1121px; height: 108px; background: var(--navy); }
  .header-rule { position: absolute; left: 0; top: 108px; width: 1121px; height: 8px; background: var(--grey); }

  .brand { position: absolute; left: 112px; top: 0; width: 250px; height: 248px; background: var(--navy);
    box-shadow: 0 2px 6px rgba(0,0,0,0.35); z-index: 3; display: flex; flex-direction: column; align-items: center; justify-content: center; gap: 18px; }
  .brand-mark { width: 110px; height: 110px; border-radius: 50%; background: var(--grey); }
  .brand-name { font-size: 27px; font-weight: 700; color: var(--red); letter-spacing: 0.5px; line-height: 1; }
  .brand-tagline { font-size: 10px; font-weight: 600; color: var(--red); letter-spacing: 0.6px; margin-top: -12px; }

  .contact-bar { position: absolute; top: 10px; left: 743px; display: flex; align-items: center; gap: 6px; color: var(--white); font-size: 19px; }
  .icon-circle { width: 28px; height: 28px; border-radius: 50%; background: var(--grey); display: flex; align-items: center; justify-content: center; }
  .social { position: absolute; display: flex; gap: 6px; }
  .social.top { left: 926px; top: 10px; }
  .social.bottom { left: 941px; top: 1148px; }
  .social span { width: 28px; height: 28px; border-radius: 50%; background: var(--grey); display: block; }

  .main-nav { position: absolute; top: 67px; left: 431px; height: 41px; display: flex; }
  .main-nav a { color: var(--white); text-decoration: none; font-size: 16px; line-height: 41px; padding: 0 14px; margin-right: 18px; }
  .main-nav a.current { background: var(--grey); color: var(--ink); margin-right: 20px; }

  .hero { position: absolute; left: 0; top: 116px; width: 1121px; height: 388px; }
  .hero-photo { position: absolute; inset: 0;
    background: linear-gradient(180deg, #6f9fd3 0%, #a8c6e6 55%, #7d8a98 66%, #9ea3a9 80%, #8d9198 100%); }
  .hero-caption { position: absolute; left: 644px; top: 132px; width: 367px; height: 117px; background: var(--caption-bg); color: var(--white); padding: 14px 22px; }
  .hero-caption h2 { font-size: 26px; font-weight: 400; letter-spacing: 0.3px; line-height: 1.2; }
  .hero-caption p { font-size: 14px; line-height: 21px; margin-top: 6px; }
  .hero-arrow { position: absolute; top: 172px; width: 44px; height: 44px; background: rgba(58,48,140,0.9); display: flex; align-items: center; justify-content: center; }
  .hero-arrow.prev { left: 0; }
  .hero-arrow.next { right: 0; }

  .about { position: absolute; left: 0; top: 504px; width: 1121px; height: 131px; background: var(--navy); color: var(--white); padding: 14px 112px 0 122px; }
  .about h1 { font-size: 22px; font-weight: 600; line-height: 1.3; }
  .about p { font-size: 14px; line-height: 20.5px; margin-top: 5px; }

  .services { position: absolute; left: 0; top: 635px; width: 1121px; height: 307px; }
  .services h3 { position: absolute; left: 112px; top: 28px; font-size: 22px; font-weight: 400; color: var(--ink-soft); }
  .service-card { position: absolute; top: 70px; width: 210px; }
  .service-photo { width: 100%; height: 134px; }
  .service-card h4 { font-size: 14px; font-weight: 700; margin-top: 9px; }
  .service-card p { font-size: 12px; line-height: 15px; color: var(--ink-soft); margin-top: 4px; }

  .partners { position: absolute; left: 0; top: 942px; width: 1121px; height: 183px; background: var(--grey-light); }
  .partners h3 { position: absolute; top: 20px; width: 100%; text-align: center; font-size: 22px; font-weight: 400; color: var(--ink-soft); }
  .partner-badge { position: absolute; top: 84px; background: #c8c8cc; }

  .site-footer { position: absolute; left: 0; top: 1125px; width: 1121px; height: 75px; background: var(--navy); }
  .footer-nav { position: absolute; left: 112px; top: 24px; display: flex; gap: 0; }
  .footer-nav a { color: var(--white); text-decoration: none; font-size: 16px; margin-right: 41px; }
</style>
</head>
<body>
<div class="page">
  <header class="site-header">
    <div class="contact-bar">
      <span class="icon-circle">
        <svg width="16" height="14" viewBox="0 0 16 14"><path d="M1 5 Q8 -1 15 5 L13 7 L11 5.5 L11 4 Q8 3 5 4 L5 5.5 L3 7 Z" fill="#1b0c63"/><rect x="4" y="7" width="8" height="6" rx="1" fill="#1b0c63"/></svg>
      </span>
      <span>+30 555 0187</span>
    </div>
    <div class="social top"><span aria-label="Social link"></span><span aria-label="Social link"></span></div>
    <nav class="main-nav">
      <a class="current" href="#">Home</a>
      <a href="#">About Us</a>
      <a href="#">Services/Capability</a>
      <a href="#">Gallery</a>
      <a href="#">Contact us</a>
    </nav>
  </header>
  <div class="header-rule"></div>

  <div class="brand">
    <div class="brand-mark"></div>
    <div class="brand-name">CORVALE AIR</div>
    <div class="brand-tagline">AIRCRAFT MAINTENANCE</div>
  </div>

  <section class="hero">
    <div class="hero-photo" role="img" aria-label="White twin-engine business jet parked on an airport apron under a blue sky"></div>
    <div class="hero-caption">
      <h2>SKYWARD TWIN ENGINE</h2>
      <p>Todit aut be sed quia consequuntur magni dolores qui ratione voluptatem sequi nesciunt.</p>
    </div>
    <a class="hero-arrow prev" href="#" aria-label="Previous slide"><svg width="16" height="28" viewBox="0 0 16 28"><path d="M14 1 L2 14 L14 27" fill="none" stroke="#c9c9e6" stroke-width="1.5"/></svg></a>
    <a class="hero-arrow next" href="#" aria-label="Next slide"><svg width="16" height="28" viewBox="0 0 16 28"><path d="M2 1 L14 14 L2 27" fill="none" stroke="#c9c9e6" stroke-width="1.5"/></svg></a>
  </section>

  <section class="about">
    <h1>About Us</h1>
    <p>Eaque ipsa quae ab illo inventore vitae dicta sunt explicabo. Nemo enim ipsam voluptatem quia voluptas sit aspernatur aut odit aut be sed quia consequuntur magni dolores eos qui ratione voluptatem sequi nesciunt. Neque porro quisquam est, qui dolorem ipsum quia dolor sit amet, consectetur, adipisci velit, sed quia non numquam eius modi.</p>
  </section>

  <section class="services">
    <h3>Services we offer</h3>
    <article class="service-card" style="left:115px;width:208px">
      <div class="service-photo" role="img" aria-label="Aircraft fuselage being prepared for paint inside a hangar" style="background:linear-gradient(180deg,#9a9ea3,#c3c4bc 55%,#8a8c88)"></div>
      <h4>Body Paint</h4>
      <p>Eaque ipsa quae ab illo inventore vitae dicta sunt explicabo.</p>
    </article>
    <article class="service-card" style="left:344px;width:208px">
      <div class="service-photo" role="img" aria-label="Engineer working on an exposed aircraft engine" style="background:linear-gradient(135deg,#cfd3d6,#6f6a5f 50%,#3e3a34)"></div>
      <h4>Engine Repair</h4>
      <p>Eaque ipsa quae ab illo inventore vitae dicta sunt explicabo.</p>
    </article>
    <article class="service-card" style="left:573px;width:208px">
      <div class="service-photo" role="img" aria-label="Technician fitting a propeller and wheel on a small aircraft" style="background:linear-gradient(180deg,#b9c2cc,#d8d8d8 50%,#6c6f78)"></div>
      <h4>Wheels and Blade Repair</h4>
      <p>Eaque ipsa quae ab illo inventore vitae dicta sunt explicabo.</p>
    </article>
    <article class="service-card" style="left:799px;width:210px">
      <div class="service-photo" role="img" aria-label="Twin turboprop aircraft with engine cowling open" style="background:linear-gradient(180deg,#e4e4e2,#b7b5ad 55%,#5d5a52)"></div>
      <h4>Engine Maintenance</h4>
      <p>Eaque ipsa quae ab illo inventore vitae dicta sunt explicabo.</p>
    </article>
  </section>

  <section class="partners">
    <h3>Company we work with:</h3>
    <div class="partner-badge" aria-label="Partner badge" style="left:108px;width:120px;height:48px;border-radius:4px"></div>
    <div class="partner-badge" aria-label="Partner badge" style="left:285px;width:74px;height:58px;top:79px;border-radius:50%"></div>
    <div class="partner-badge" aria-label="Partner badge" style="left:430px;width:74px;height:52px;top:82px;border-radius:4px"></div>
    <div class="partner-badge" aria-label="Partner badge" style="left:582px;width:98px;height:58px;top:79px;border-radius:4px"></div>
    <div class="partner-badge" aria-label="Partner badge" style="left:751px;width:66px;height:52px;top:82px"></div>
    <div class="partner-badge" aria-label="Partner badge" style="left:885px;width:122px;height:36px;top:90px;border-radius:4px"></div>
  </section>

  <footer class="site-footer">
    <nav class="footer-nav">
      <a href="#">Home</a>
      <a href="#">About Us</a>
      <a href="#">Services/Capability</a>
      <a href="#">Gallery</a>
      <a href="#">Contact us</a>
    </nav>
  </footer>
  <div class="social bottom"><span aria-label="Social link"></span><span aria-label="Social link"></span></div>
</div>
</body>
</html>
```